Business Landing Page for SEO Company

Need the landing page of the website designed - I will provide the copy, will need to include details of my company and the services offered, about us, testimonials, faq, etc., and all these elements will need to be arranged graphically on the page.

I want something similar to this: https://pebrovault.com/

Not in terms of color or theme or anything, but we offer a similar service and want to display similar information.

Th services we provide are:

Premium Links
Monthly Links Subscription
Link Insertions

Need to advertise them on the front page. Additionally need a place for testimonials, company details, etc.,

We already have logo for the website. Please use the attached file to insert the logo within the overal design.

Target Market(s)

SEO marketers and agencies

Number of Pages Required

1 page

```html
<!DOCTYPE html>
<html lang="en">
<head>
<meta charset="utf-8">
<title>Ranktide – SEO Link Building</title>
<link href="https://fonts.googleapis.com/css2?family=Montserrat:wght@400;500;600;700&family=Arvo:wght@700&display=swap" rel="stylesheet">
<style>
:root{
  --blue:#2b86e0;
  --orange:#f5820d;
  --ink:#222428;
  --muted:#8d8f93;
  --line:#e4e4e4;
  --soft:#f5f5f5;
  --dark:#2b2f35;
  --white:#ffffff;
}
*{margin:0;padding:0;box-sizing:border-box}
html,body{width:1200px;height:5213px;overflow:hidden}
body{position:relative;background:var(--white);font-family:"Montserrat",sans-serif;color:var(--ink)}
.abs{position:absolute}
.shapes{position:absolute;left:0;top:0;width:1200px;height:5213px}
.photo{position:absolute;background:linear-gradient(135deg,#b9bcc2,#6f747c)}
.wordmark{font-family:"Montserrat",sans-serif;font-weight:600;font-size:34px;color:var(--blue);line-height:1;letter-spacing:.5px}
.wordmark.light{color:var(--white)}
.para{font-size:11.5px;line-height:20px;color:var(--muted)}
.btn{position:absolute;background:var(--orange);color:var(--white);font-size:12px;font-weight:600;text-transform:uppercase;display:flex;align-items:center;justify-content:center;letter-spacing:.3px}
.h-wide{font-family:"Montserrat",sans-serif;font-weight:600;font-size:34px;letter-spacing:1.5px;line-height:38px}
.blue{color:var(--blue)}.orange{color:var(--orange)}

/* hero */
.hero-photo{left:0;top:0;width:1200px;height:720px;background:linear-gradient(160deg,#5a5d62 0%,#2f3136 45%,#76797e 100%)}
.nav{position:absolute;top:45px;left:596px;display:flex;gap:30px;font-size:11px;color:var(--white);text-transform:uppercase;letter-spacing:.3px}
.nav .active{color:var(--blue);border-bottom:2px solid var(--blue);padding-bottom:4px}
.search{left:1101px;top:35px;width:36px;height:36px;border-radius:50%;background:var(--orange)}
.hero-box{left:470px;top:182px;width:261px;height:334px;background:var(--orange);opacity:.92}
.hero-copy{left:0;top:243px;width:1200px;text-align:center;color:var(--white)}
.hero-kicker{font-family:"Arvo",serif;font-weight:400;font-size:17px;letter-spacing:.5px}
.hero-title{font-family:"Arvo",serif;font-weight:700;font-size:46px;line-height:54px;margin-top:12px}
.hero-btn{left:518px;top:410px;width:164px;height:44px;border:1.5px solid var(--white);color:var(--white);font-size:12px;display:flex;align-items:center;justify-content:center;text-transform:uppercase}
.hero-arrow{width:38px;height:38px;border:1.5px solid rgba(255,255,255,.75);border-radius:50%;background:rgba(255,255,255,.12)}

/* welcome & about */
.welcome-title{left:136px;top:760px}
.welcome-text{left:466px;top:755px;width:592px}
.divider{left:136px;top:909px;width:928px;height:1px;background:var(--line)}
.frame{position:absolute;background:var(--white);box-shadow:0 2px 8px rgba(0,0,0,.18);padding:8px}
.frame .photo{position:relative;width:100%;height:100%}
.about-title{left:640px;top:972px;font-size:26px;font-weight:400}
.about-text{left:637px;top:1022px;width:430px}

/* getting started */
.started-title{left:136px;top:1448px}
.started-text{left:136px;top:1508px;width:460px}
.play{left:836px;top:1571px;width:68px;height:68px;border-radius:50%;background:var(--orange);border:3px solid var(--white)}

/* services */
.center{left:0;width:1200px;text-align:center}
.card{position:absolute;top:2064px;width:285px;height:407px;background:var(--white);box-shadow:0 1px 6px rgba(0,0,0,.1);border-bottom:4px solid var(--blue);text-align:center}
.card .photo{position:relative;width:100%;height:193px}
.card h3{font-size:17px;font-weight:500;margin-top:30px}
.card p{width:240px;margin:12px auto 0}
.card svg{margin-top:14px}

/* feedback */
.review{left:210px;top:2701px;width:780px;height:187px;background:var(--white);box-shadow:0 2px 10px rgba(0,0,0,.12)}
.review .photo{left:0;top:0;width:188px;height:187px;border-right:4px solid var(--orange);background:linear-gradient(135deg,#c8c3bd,#7b7671)}
.review .para{position:absolute;left:237px;top:36px;width:500px}
.review .who{position:absolute;left:237px;top:133px;font-size:12px;color:var(--blue);font-weight:600}

/* call */
.call{top:3098px;font-size:30px;line-height:39px;color:var(--ink)}

/* contact */
.contact-photo{left:0;top:3320px;width:1200px;height:542px;background:linear-gradient(150deg,#3a3e45,#23262b)}
.info{position:absolute;left:136px;display:flex;gap:18px;align-items:center}
.info .ico{width:34px;height:34px;background:var(--orange);display:flex;align-items:center;justify-content:center}
.info .lab{font-size:10px;color:var(--orange);text-transform:uppercase}
.info .val{font-size:12px;color:var(--white);margin-top:6px}
.field{position:absolute;background:var(--white);font-size:10.5px;color:var(--muted);padding:12px 14px}

/* footer */
.foot-links{top:4008px;font-size:11.5px;color:#555}
.social{position:absolute;width:36px;height:36px}
.copyband{left:0;top:4157px;width:1200px;height:57px;background:var(--blue);color:var(--white);font-size:10px;display:flex;align-items:center;justify-content:center}

/* blog */
.blog-title{top:4288px;font-family:"Arvo",serif;font-size:30px}
.mini{position:absolute;left:61px;display:flex;gap:26px}
.mini .photo{position:relative;width:89px;height:89px}
.mini .date,.post .date{font-size:11px;color:var(--blue)}
.mini .t{font-size:11.5px;font-weight:600;line-height:23px;margin-top:8px;width:210px}
.post{position:absolute;top:4388px;width:337px}
.post .photo{position:relative;width:100%;height:224px}
.post .badge{position:absolute;left:9px;top:9px;background:var(--orange);color:var(--white);font-size:10px;padding:3px 10px}
.post .t{font-size:14px;font-weight:600;line-height:26px;margin-top:28px}
.post .more{font-size:10px;font-weight:600;color:var(--blue);margin-top:12px;text-transform:uppercase}

/* big footer */
.bigfoot{left:0;top:4798px;width:1200px;height:415px;background:var(--blue)}
.fcol{position:absolute;top:4874px;color:var(--white)}
.fcol h4{font-size:19px;font-weight:500;margin-bottom:18px}
.fcol li{list-style:none;font-size:11px;line-height:23px}
.fcol li::before{content:"›";margin-right:8px}
.touch{position:absolute;left:888px;display:flex;gap:16px;color:var(--white);font-size:11px;line-height:20px}
.touch .ico{width:28px;height:28px;background:var(--white);display:flex;align-items:center;justify-content:center;flex:none}
.fsocial{position:absolute;top:4944px;width:28px;height:28px;border:1.5px solid rgba(255,255,255,.7);background:rgba(255,255,255,.12)}
.fcopy{top:5178px;font-size:10px;color:var(--white)}
</style>
</head>
<body>

<!-- hero -->
<div class="photo hero-photo" role="img" aria-label="Black and white skyscrapers seen from street level"></div>
<svg class="shapes" viewBox="0 0 1200 5213" aria-hidden="true">
  <polygon points="0,603 1200,712 1200,1290 0,1290" fill="#ffffff"/>
  <polygon points="570,652 1170,706 1170,726" fill="#2b86e0"/>
</svg>
<div class="abs wordmark light" style="left:60px;top:34px">Ranktide</div>
<nav class="nav">
  <span class="active">Home</span><span>About</span><span>Services</span><span>Testimonials</span><span>Blog</span><span>Contact Us</span>
</nav>
<div class="abs search">
  <svg width="36" height="36" viewBox="0 0 36 36"><circle cx="17" cy="17" r="6" fill="none" stroke="#fff" stroke-width="2"/><line x1="21.5" y1="21.5" x2="25" y2="25" stroke="#fff" stroke-width="2"/></svg>
</div>
<div class="abs hero-box"></div>
<div class="abs hero-copy">
  <div class="hero-kicker">WE HANDLE THE SEO COMAPNY</div>
  <div class="hero-title">So You Can Focus on<br>Your Business</div>
</div>
<div class="abs hero-btn">Contact Us Now!</div>
<div class="abs hero-arrow" style="left:60px;top:329px"><svg width="36" height="36"><polyline points="20,12 14,18 20,24" fill="none" stroke="#fff" stroke-width="1.6"/></svg></div>
<div class="abs hero-arrow" style="left:1100px;top:329px"><svg width="36" height="36"><polyline points="16,12 22,18 16,24" fill="none" stroke="#fff" stroke-width="1.6"/></svg></div>
<svg class="abs" style="left:579px;top:638px" width="42" height="42" viewBox="0 0 42 42" aria-hidden="true">
  <circle cx="21" cy="21" r="20" fill="#fff" stroke="#f5820d" stroke-width="1.5"/>
  <rect x="15" y="11" width="12" height="19" rx="6" fill="none" stroke="#f5820d" stroke-width="1.6"/>
  <line x1="21" y1="14" x2="21" y2="18" stroke="#f5820d" stroke-width="1.6"/>
</svg>

<!-- welcome -->
<h1 class="abs h-wide welcome-title"><span class="blue">Welcome To</span><br><span class="orange">Ranktide</span></h1>
<p class="abs para welcome-text">Lorem ipsum dolor sit amet, consectetur adipiscing elit, sed do eiusmod tempor incididunt ut labore et dolore magna aliqua. Ut enim ad minim veniam, quis nostrud exercitation ullamco laboris nisi ut aliquip ex ea commodo consequat. Duis aute irure dolor in reprehenderit in voluptate velit esse cillum dolore eu fugiat nulla pariatur.</p>
<div class="abs divider"></div>

<!-- about -->
<div class="frame" style="left:136px;top:975px;width:335px;height:225px"><div class="photo" role="img" aria-label="Business team meeting around a flip chart"></div></div>
<div class="frame" style="left:390px;top:1073px;width:165px;height:159px"><div class="photo" role="img" aria-label="Two business people shaking hands" style="background:linear-gradient(135deg,#c5d2de,#5e6f82)"></div></div>
<h2 class="abs about-title">About Company</h2>
<div class="abs about-text para">
  <p>Lorem ipsum dolor sit amet, consectetur adipiscing elit, sed do eiusmod tempor incididunt ut labore et dolore magna aliqua. Ut enim ad minimed veniam, quis nostrud exercitation ullamco laboris nisi ut aliquip.</p>
  <p style="margin-top:14px">Lorem ipsum dolor sit amet, consectetur adipiscing elit, sed do eiusmod tempor incididunt ut labore et dolore magna aliqua. Ut enim ad minimed veniam, quis nostrud exercitation ullamco laboris.</p>
</div>
<div class="btn" style="left:637px;top:1194px;width:120px;height:41px">Learn More</div>

<!-- getting started -->
<svg class="shapes" viewBox="0 0 1200 5213" aria-hidden="true">
  <polygon points="0,1290 1200,1402 1200,1846 0,1846" fill="#f5f5f5"/>
  <polygon points="30,1276 1200,1396 1200,1402 30,1296" fill="#2b86e0"/>
  <polygon points="0,2550 1200,2550 1200,3030 0,2944" fill="#f5f5f5"/>
  <polygon points="0,2944 1170,3050 1170,3072 0,2950" fill="#2b86e0"/>
</svg>
<h2 class="abs h-wide orange started-title">Getting Started</h2>
<div class="abs started-text para">
  <p>Lorem ipsum dolor sit amet, consectetur adipiscing elit, sed do eiusmod theird tempor incididunt ut labore et dolore magna aliqua. Ut enim ad minim veniam, quis nostrud exercitation ullamco laboris nisi ut aliquip ex ea commodo to the consequat. Duis aute irure dolor in reprehenderit in voluptate velit esse cillum dolore eu fugiat nulla pariatur. Excepteur sint occaecat cupidatat non proiden.</p>
  <p style="margin-top:14px">Lorem ipsum dolor sit amet, consectetur adipiscing elit, sed do eiusmod theird tempor incididunt ut labore et dolore magna aliqua. Ut enim ad minim veniam, quis nostrud exercitation ullamco laboris.</p>
</div>
<div class="btn" style="left:136px;top:1718px;width:157px;height:45px">Watch Our Video</div>
<div class="photo" role="img" aria-label="Overhead view of a desk with laptop, coffee cups and hands at work" style="left:674px;top:1447px;width:390px;height:316px;background:linear-gradient(135deg,#8a7a66,#c9c2b6 55%,#6c6a66)"></div>
<div class="abs play"><svg width="62" height="62" viewBox="0 0 62 62"><polygon points="25,19 43,31 25,43" fill="#fff"/></svg></div>

<!-- services -->
<h2 class="abs center h-wide" style="top:1920px"><span class="blue">We Provide</span> <span class="orange">Services</span></h2>
<p class="abs center para" style="top:1984px;padding:0 330px">Lorem ipsum dolor sit amet, consectetur adipiscing elit, sed do eiusmod tempor incididunt ut labore et dolore magna aliqua. Ut enim ad minim veniam, quis nostrud exercitation.</p>

<div class="card" style="left:136px">
  <div class="photo" role="img" aria-label="Woman working at a laptop"></div>
  <h3>Premium Links</h3>
  <p class="para">Lorem ipsum dolor sit amet, consectetur adipiscing elit, sed do eiusmod tempor incididunt dolore magna aliqua.</p>
  <svg width="62" height="62" viewBox="0 0 62 62" fill="none" stroke="#f5820d" stroke-width="2">
    <path d="M31 3 L36 9 L44 7 L46 15 L54 18 L51 26 L56 32 L50 38 L52 46 L44 48 L41 56 L33 53 L27 58 L22 51 L14 51 L13 43 L6 38 L10 31 L6 23 L13 19 L14 11 L22 11 L27 4 Z"/>
    <polygon points="31,19 34.5,27 43,27.5 36.5,33 38.5,41 31,36.5 23.5,41 25.5,33 19,27.5 27.5,27"/>
  </svg>
</div>
<div class="card" style="left:457px">
  <div class="photo" role="img" aria-label="Two businessmen reviewing work at a laptop" style="background:linear-gradient(135deg,#9aa4ae,#464c55)"></div>
  <h3>Monthly Links Subscription</h3>
  <p class="para">Lorem ipsum dolor sit amet, consectetur adipiscing elit, sed do eiusmod tempor incididunt dolore magna aliqua.</p>
  <svg width="62" height="62" viewBox="0 0 62 62" fill="none" stroke="#f5820d" stroke-width="2">
    <rect x="4" y="8" width="54" height="48" rx="3"/>
    <line x1="4" y1="18" x2="58" y2="18"/>
    <line x1="16" y1="4" x2="16" y2="12"/><line x1="46" y1="4" x2="46" y2="12"/>
    <line x1="4" y1="30" x2="58" y2="30"/><line x1="4" y1="43" x2="58" y2="43"/>
    <line x1="17" y1="18" x2="17" y2="56"/><line x1="31" y1="18" x2="31" y2="56"/><line x1="45" y1="18" x2="45" y2="56"/>
  </svg>
</div>
<div class="card" style="left:779px">
  <div class="photo" role="img" aria-label="Hand holding a smartphone" style="background:linear-gradient(135deg,#c8ccd2,#6a7078)"></div>
  <h3>Link Insertions</h3>
  <p class="para">Lorem ipsum dolor sit amet, consectetur adipiscing elit, sed do eiusmod tempor incididunt dolore magna aliqua.</p>
  <svg width="62" height="62" viewBox="0 0 62 62" fill="none" stroke="#f5820d" stroke-width="2">
    <polygon points="10,28 40,10 46,40 20,42"/>
    <path d="M10 28 L6 36 L12 44 L20 42"/>
    <path d="M14 43 L20 56 L27 53 L22 42"/>
    <line x1="50" y1="18" x2="57" y2="14"/><line x1="52" y1="26" x2="59" y2="26"/><line x1="50" y1="34" x2="56" y2="38"/>
  </svg>
</div>

<!-- feedback -->
<h2 class="abs center h-wide" style="top:2626px"><span class="blue">Client's</span> <span class="orange">Feedback</span></h2>
<div class="abs review">
  <div class="photo" role="img" aria-label="Portrait of a smiling client"></div>
  <p class="para">Lorem ipsum dolor sit amet, consectetur adipiscing elit, sed do eiusmod tempor incididunt ut labore et dolore magna aliqua. Ut enim ad minim veniam, quis nostrud exercitation ullamco laboris nisi ut aliquip ex ea commodo consequat. Duis aute irure dolor in reprehenderit in voluptate velit esse cillum dolore eu fugiat nulla pariatur.</p>
  <div class="who">-&nbsp; Client Name</div>
</div>
<svg class="abs" style="left:166px;top:2781px" width="24" height="32" aria-hidden="true"><polyline points="18,2 6,16 18,30" fill="none" stroke="#f5820d" stroke-width="2.5"/></svg>
<svg class="abs" style="left:1010px;top:2781px" width="24" height="32" aria-hidden="true"><polyline points="6,2 18,16 6,30" fill="none" stroke="#2b86e0" stroke-width="2.5"/></svg>

<!-- call to action -->
<div class="abs" style="left:127px;top:3107px;width:33px;height:32px;background:var(--orange)"></div>
<div class="abs" style="left:164px;top:3107px;width:34px;height:32px;background:var(--blue)"></div>
<p class="abs center call">Call today to Discuss your business<br>Services Needs We look Forward to<br>hearing from You!</p>

<!-- contact -->
<div class="photo contact-photo" role="img" aria-label="Dark photo of a team working at a table"></div>
<svg class="shapes" viewBox="0 0 1200 5213" aria-hidden="true">
  <polygon points="0,3310 1200,3310 1200,3446 0,3330" fill="#ffffff"/>
  <polygon points="30,3314 1200,3436 1200,3444 30,3334" fill="#2b86e0"/>
</svg>
<h2 class="abs center h-wide blue" style="top:3472px">Contact Us</h2>
<p class="abs center para" style="top:3536px;padding:0 365px;color:#d5d6d8">Lorem ipsum dolor sit amet, consectetur adipiscing elit, sed do eiusmod tempor incididunt ut labore et dolore magna aliqua Ut enim ad minim veniam.</p>

<div class="info" style="top:3620px">
  <div class="ico"><svg width="18" height="20" viewBox="0 0 18 20"><path d="M9 1a6 6 0 0 0-6 6c0 5 6 12 6 12s6-7 6-12a6 6 0 0 0-6-6z" fill="#fff"/><circle cx="9" cy="7" r="2.3" fill="#f5820d"/></svg></div>
  <div><div class="lab">Address</div><div class="val">123,street,state,city,zipcode</div></div>
</div>
<div class="info" style="top:3681px">
  <div class="ico"><svg width="18" height="18" viewBox="0 0 18 18"><path d="M4 1l3 4-2 2c1 3 3 5 6 6l2-2 4 3-2 3C8 17 1 10 1 3z" fill="#fff"/></svg></div>
  <div><div class="lab">Phone</div><div class="val">123.456.7890</div></div>
</div>
<div class="info" style="top:3741px">
  <div class="ico"><svg width="20" height="14" viewBox="0 0 20 14"><rect x="1" y="1" width="18" height="12" fill="none" stroke="#fff" stroke-width="1.6"/><polyline points="1,1 10,8 19,1" fill="none" stroke="#fff" stroke-width="1.6"/></svg></div>
  <div><div class="lab">Email</div><div class="val">info@ranktide.com</div></div>
</div>

<div class="field" style="left:453px;top:3617px;width:294px;height:43px">Name* &nbsp;:</div>
<div class="field" style="left:453px;top:3677px;width:294px;height:43px">Email* &nbsp;:</div>
<div class="field" style="left:453px;top:3738px;width:294px;height:43px">Phone* &nbsp;:</div>
<div class="field" style="left:773px;top:3617px;width:293px;height:103px">Message / comments &nbsp;:</div>
<div class="btn" style="left:773px;top:3738px;width:127px;height:43px">Submit Now</div>

<!-- footer -->
<div class="abs center" style="top:3942px"><div class="wordmark" style="display:inline-block">Ranktide</div></div>
<p class="abs center foot-links">Home &nbsp;|&nbsp; About &nbsp;|&nbsp; Services &nbsp;|&nbsp; Testimonials &nbsp;|&nbsp; Blog &nbsp;|&nbsp; Contact Us</p>
<div class="social" style="left:536px;top:4044px;background:#4a62a8" aria-label="Social profile one"></div>
<div class="social" style="left:582px;top:4044px;background:#3aa7e6" aria-label="Social profile two"></div>
<div class="social" style="left:628px;top:4044px;background:#1f78b9" aria-label="Social profile three"></div>
<div class="abs copyband">Copyright © RANKTIDE - 2021 . All right reserved. Privacy Policy. &nbsp;terms &amp; conditions.</div>

<!-- recent blog -->
<h2 class="abs center blog-title">Recent Blog</h2>
<div class="mini" style="top:4388px">
  <div class="photo" role="img" aria-label="Phone on a desk"></div>
  <div><div class="date" style="margin-top:14px">14 Jan 2021</div><div class="t">Lorem ipsum dolor consectetur adipiscing eiusmod tempor.</div></div>
</div>
<div class="mini" style="top:4512px">
  <div class="photo" role="img" aria-label="Coffee cup and notebook" style="background:linear-gradient(135deg,#b89a80,#6e5443)"></div>
  <div><div class="date" style="margin-top:14px">14 Jan 2021</div><div class="t">Lorem ipsum dolor consectetur adipiscing eiusmod tempor.</div></div>
</div>
<div class="mini" style="top:4635px">
  <div class="photo" role="img" aria-label="Laptop on a wooden table" style="background:linear-gradient(135deg,#c79a6c,#5c3f28)"></div>
  <div><div class="date" style="margin-top:14px">14 Jan 2021</div><div class="t">Lorem ipsum dolor consectetur adipiscing eiusmod tempor.</div></div>
</div>
<div class="post" style="left:431px">
  <div class="photo" role="img" aria-label="Team talking around an office table" style="background:linear-gradient(135deg,#bfb7ad,#5d5750)"></div>
  <div class="badge">14 Jan 2021</div>
  <div class="t">Lorem ipsum dolor sit amet, consectetur adipiscing elit, sed do eiusmod tempor.</div>
  <div class="more">Learn More ▸</div>
</div>
<div class="post" style="left:803px">
  <div class="photo" role="img" aria-label="Man working at a desktop computer" style="background:linear-gradient(135deg,#e2e4e6,#8c9196)"></div>
  <div class="badge">14 Jan 2021</div>
  <div class="t">Lorem ipsum dolor sit amet, consectetur adipiscing elit, sed do eiusmod tempor.</div>
  <div class="more">Learn More ▸</div>
</div>

<!-- blue footer -->
<div class="abs bigfoot"></div>
<div class="abs wordmark light" style="left:61px;top:4878px">Ranktide</div>
<div class="fsocial" style="left:61px"></div>
<div class="fsocial" style="left:99px"></div>
<div class="fsocial" style="left:136px"></div>
<div class="fsocial" style="left:174px"></div>

<div class="fcol" style="left:336px">
  <h4>Services</h4>
  <ul><li>Premium Links</li><li>Monthly Links Subscription</li><li>Link Insertions</li></ul>
</div>
<div class="fcol" style="left:613px">
  <h4>Links</h4>
  <ul><li>Home</li><li>About</li><li>Services</li><li>Testimonials</li><li>Blog</li><li>Contact Us</li></ul>
</div>
<div class="fcol" style="left:888px"><h4>Get In Touch</h4></div>
<div class="touch" style="top:4922px">
  <div class="ico"><svg width="14" height="16" viewBox="0 0 18 20"><path d="M9 1a6 6 0 0 0-6 6c0 5 6 12 6 12s6-7 6-12a6 6 0 0 0-6-6z" fill="#f5820d"/><circle cx="9" cy="7" r="2.3" fill="#fff"/></svg></div>
  <div>123,Address,Street Name, State<br>Name, City Name, Zipcode.</div>
</div>
<div class="touch" style="top:4983px">
  <div class="ico"><svg width="14" height="14" viewBox="0 0 18 18"><path d="M4 1l3 4-2 2c1 3 3 5 6 6l2-2 4 3-2 3C8 17 1 10 1 3z" fill="#f5820d"/></svg></div>
  <div>PHONE<br>123.456.7890</div>
</div>
<div class="touch" style="top:5044px">
  <div class="ico"><svg width="16" height="12" viewBox="0 0 20 14"><rect x="1" y="1" width="18" height="12" fill="none" stroke="#f5820d" stroke-width="1.8"/><polyline points="1,1 10,8 19,1" fill="none" stroke="#f5820d" stroke-width="1.8"/></svg></div>
  <div>EMAIL<br>hello@ranktide.com</div>
</div>
<p class="abs center fcopy">Copyright © RANKTIDE - 2021 . All right reserved. Privacy Policy. &nbsp;terms &amp; conditions.</p>

</body>
</html>
```